Hi, everyone!

We're looking for a tenacious designer to help us create two (2) 33 x 86 single-sided retractable banners. The banners will be purchased through
Bannerloft (see: https://www.bannerloft-example.ca/signs-posters/retractable-banners?xnav=swsProductOnly_ResultTitle).

I have attached a wide variety of materials including the Plovrix - Creative Production logos (.psd files), previous attempts at making a banner including some handwritten notes and a table cloth that will be used in the same space as the banners and the back of our business card to give you an idea of our colours.

Note: We like the colours used on the other banner designs but do not like the layout or icons - they look cluttered and unprofessional. They are good as a guide but not what we want as a design. Similarly, avoid featuring close-ups of people from stock photos.

At least one of the banners must feature: (you can use icons instead of words if it means a better design)

www.plovrix-example.ca
Email: get@plovrix-example.ca
Phone: (555) 214-0873
Social Media Handle: plovrixstudio

There is also a word document on the bottom to guide some of the copywriting that may be used. If you're really ambitious, we're happy to consider different phrases and copy.

Finally, the fonts that we use are:
Plovrix Logo - Metropolis
Titles: Adelle Font Family
Body / Content: Avenir Font Family

As with everything, we welcome other suggestions or recommendations.

Target Market(s)

Government, Small Business, Non-Profits, Indigenous Canadian Communities

Font styles to use
Sans Serif

Colors

Designer to choose colors to be used in the design.

Requirements
Must have
• The deliverables for this project are:
• - Two (2) 33 x 86 Single-Sided Retractable Banners
• They will be purchased through Bannerloft Canada (see: https://www.bannerloft-example.ca/signs-posters/retractable-banners?xnav=swsProductOnly_ResultTitle). You may want to try loading your design there before submitting them to us.
Nice to have
• We like the colours of the initial designs but they are unprofessional, cluttered and from a template. Ideally, we would like a unique design that works with the colours in our logo (red, black, white and yellow).
• One banner may focus on Tourism Development and the other could feature Creative Strategy.
Should not have
• Please do not use stock photos that feature people - our target market is put off by such pictures. If you'd like an idea of our tourism focus, visit:
• - https://northwoodtravelcircle-example.ca/en/
• - https://lakeheadjourneys-example.ca/
• - https://www.qolfa-example.org/

```html
<!DOCTYPE html>
<html lang="en">
<head>
<meta charset="utf-8">
<title>Plovrix – Retractable Banner</title>
<link rel="stylesheet" href="https://fonts.googleapis.com/css2?family=Arimo:wght@400;700&display=swap">
<style>
  :root {
    --page-bg: #e9eaec;
    --banner-white: #f4f3f3;
    --brand-red: #d3142c;
    --brand-orange: #e36a22;
    --brand-black: #2a2626;
    --footer-grey: #3b3a3a;
    --ink: #1d1d1d;
    --white: #ffffff;
  }
  * { box-sizing: border-box; margin: 0; padding: 0; }
  html, body { width: 1200px; height: 800px; overflow: hidden; }
  body {
    background: var(--page-bg);
    font-family: "Arimo", Arial, sans-serif;
    position: relative;
  }
  .banner {
    position: absolute;
    left: 452px;
    top: 20px;
    width: 450px;
    height: 1155px;
    transform: scale(0.658);
    transform-origin: 0 0;
    background: var(--banner-white);
    overflow: hidden;
    box-shadow: 0 6px 18px rgba(0,0,0,0.18);
  }
  .banner-art { position: absolute; left: 0; top: 0; width: 450px; height: 760px; }
  .headline {
    position: absolute; left: 30px; top: 652px;
    color: var(--brand-red);
    font-weight: 700; font-size: 27px; line-height: 33px;
    letter-spacing: 0.5px;
  }
  .headline-rule {
    position: absolute; left: 28px; top: 757px; width: 294px; height: 1.5px;
    background: var(--brand-red);
  }
  .subhead {
    position: absolute; left: 28px; top: 768px;
    color: var(--ink); font-size: 27px; line-height: 34px; font-weight: 400;
  }
  .intro {
    position: absolute; left: 28px; top: 842px; width: 402px;
    color: var(--ink); font-size: 12.4px; line-height: 16px;
  }
  .help-tab {
    position: absolute; left: 0; top: 914px; width: 228px; height: 40px;
    background: var(--brand-red); color: var(--white);
    font-weight: 700; font-size: 19px; line-height: 40px;
    padding-left: 30px; border-radius: 0 5px 5px 0;
  }
  .services {
    position: absolute; left: 30px; top: 962px;
    list-style: none; color: var(--ink);
    font-size: 13.5px; line-height: 16px; letter-spacing: 1px;
  }
  .services li::before { content: "- "; }
  .footer {
    position: absolute; left: 0; top: 1050px; width: 450px; height: 105px;
    background: var(--footer-grey); color: var(--white);
  }
  .brand {
    position: absolute; left: 34px; top: 32px;
    display: flex; align-items: center; gap: 10px;
  }
  .brand-dot { width: 30px; height: 30px; border-radius: 50%; background: var(--brand-red); }
  .brand-name { font-size: 22px; font-weight: 700; color: var(--white); letter-spacing: 0.5px; }
  .footer-divider {
    position: absolute; left: 210px; top: 14px; width: 1px; height: 78px;
    background: rgba(255,255,255,0.7);
  }
  .contact { position: absolute; left: 230px; top: 28px; list-style: none; }
  .contact li {
    display: flex; align-items: center; gap: 9px;
    font-size: 13px; line-height: 18px; letter-spacing: 0.4px; font-weight: 400;
  }
  .contact svg { width: 13px; height: 13px; flex: none; }
  .social { position: absolute; left: 256px; top: 72px; display: flex; gap: 6px; }
  .social span { width: 20px; height: 20px; border-radius: 50%; background: var(--white); }
</style>
</head>
<body>
  <section class="banner" aria-label="Plovrix retractable banner">
    <svg class="banner-art" viewBox="0 0 450 760">
      <defs>
        <linearGradient id="landscapeTones" x1="0" y1="0" x2="0" y2="1">
          <stop offset="0" stop-color="#3a2f2a"/>
          <stop offset="0.2" stop-color="#8c6a4c"/>
          <stop offset="0.38" stop-color="#c09a70"/>
          <stop offset="0.48" stop-color="#7c7773"/>
          <stop offset="0.6" stop-color="#33502c"/>
          <stop offset="0.72" stop-color="#566f3c"/>
          <stop offset="0.82" stop-color="#3f4e5c"/>
          <stop offset="1" stop-color="#2b3947"/>
        </linearGradient>
      </defs>
      <path class="band-red" fill="var(--brand-red)" d="M0,470 C110,650 290,730 450,725 V0 H0 Z"/>
      <path class="band-orange" fill="var(--brand-orange)" d="M0,440 C110,610 270,690 450,690 V0 H0 Z"/>
      <path class="band-black" fill="var(--brand-black)" d="M0,420 C60,560 170,640 270,655 C340,650 410,628 450,612 V0 H0 Z"/>
      <path class="landscape-photo" role="img" aria-label="Photo of a mountain range under a dramatic sunset sky above a pine forest and a calm lake"
        fill="url(#landscapeTones)" d="M0,390 C70,560 210,640 330,632 C400,626 440,610 450,605 V0 H0 Z"/>
    </svg>

    <h1 class="headline">CREATIVE,<br>CULTURALLY<br>INSPIRED STRATEGY</h1>
    <div class="headline-rule"></div>
    <h2 class="subhead">We Start with<br>Your Story</h2>
    <p class="intro">At Plovrix we start with your story. It enables us to create a deeper connection, unite people and drives meaningful growth. As your Indigenous marketing, communication and event partner, we use the power of story to learn, share, elevate and innovate.</p>

    <div class="help-tab">How Can We Help?</div>
    <ul class="services">
      <li>Destination and Product Development</li>
      <li>Media and Marketing</li>
      <li>Event Management and Planning</li>
      <li>Brand Development</li>
      <li>Graphic, Print and Web Design</li>
    </ul>

    <footer class="footer">
      <div class="brand">
        <span class="brand-dot"></span>
        <span class="brand-name">Plovrix</span>
      </div>
      <div class="footer-divider"></div>
      <ul class="contact">
        <li>
          <svg viewBox="0 0 14 14" fill="none" stroke="#fff" stroke-width="1.2"><circle cx="7" cy="7" r="6"/><ellipse cx="7" cy="7" rx="2.6" ry="6"/><path d="M1 7h12M2 4h10M2 10h10"/></svg>
          plovrix-example.ca/tourism
        </li>
        <li>
          <svg viewBox="0 0 14 14" fill="none" stroke="#fff" stroke-width="1.2"><rect x="1" y="3" width="12" height="8"/><path d="M1 3l6 5 6-5"/></svg>
          get@plovrix-example.ca
        </li>
      </ul>
      <div class="social" aria-label="Social media links">
        <span></span><span></span><span></span><span></span><span></span>
      </div>
    </footer>
  </section>
</body>
</html>
```